Awesome ecommerce store banner needed!

We need a sharp, clear, strong banner for one of our subcategory pages on http://www.brivelloop.example
We'd like to incorporate the following image. We'd like the background to be gray or black. We are replacing the Wireless Intercoms banner that is orange (we hate it).
WE do like our other banners, however, so please use them as reference:
SIze: 980 x 380
Two raw images of the intercom we'd like you to encorporate have been included. Choose one or the other depending on what you think would be best. If using the single angle, please duplicate it. We want two intercoms in the banner
Simple and Clean is key:
Text: Wireless Intercoms
Text Color: Can be white/off gray
Text Style: Please keep it clean in line with the website
Background: Black/gray/white

```html
<!DOCTYPE html>
<html lang="en">
<head>
<meta charset="UTF-8">
<title>Wireless Intercoms – Brivelloop</title>
<link rel="stylesheet" href="https://fonts.googleapis.com/css2?family=Roboto:wght@900&family=Mulish:wght@400&family=Roboto+Condensed:wght@700&display=swap">
<style>
  :root {
    --bg-light: #eeeeee;
    --bg-mid: #e2e2e2;
    --headline: #6a6b6d;
    --body-text: #2e2e2e;
    --button-top: #8c8c8c;
    --button-bottom: #4f4f4f;
    --button-text: #ffffff;
    --silver-light: #d4d4d4;
    --silver-dark: #8f8f8f;
    --device-black: #1d1d1d;
  }
  * { margin: 0; padding: 0; box-sizing: border-box; }
  html, body { width: 1200px; height: 465px; overflow: hidden; }
  body { background: var(--bg-mid); }
  .banner {
    position: relative;
    width: 1200px;
    height: 465px;
    overflow: hidden;
    background: radial-gradient(ellipse at 40% 45%, var(--bg-light) 0%, var(--bg-mid) 80%);
  }
  .headline {
    position: absolute;
    left: 52px;
    top: 22px;
    font-family: "Roboto", "Arial Black", sans-serif;
    font-weight: 900;
    color: var(--headline);
    line-height: 1;
    text-transform: uppercase;
  }
  .headline__top {
    display: block;
    font-size: 122px;
    letter-spacing: -1px;
  }
  .headline__bottom {
    display: block;
    font-size: 82px;
    letter-spacing: 1px;
    margin-top: -6px;
    padding-left: 2px;
  }
  .tagline {
    position: absolute;
    left: 56px;
    top: 246px;
    font-family: "Mulish", "Helvetica Neue", sans-serif;
    font-weight: 400;
    font-size: 27px;
    line-height: 43px;
    color: var(--body-text);
  }
  .cta {
    position: absolute;
    left: 55px;
    top: 371px;
    width: 292px;
    height: 67px;
    border-radius: 4px;
    background: linear-gradient(var(--button-top), var(--button-bottom));
    color: var(--button-text);
    font-family: "Roboto Condensed", "Arial", sans-serif;
    font-weight: 700;
    font-size: 34px;
    display: flex;
    align-items: center;
    justify-content: center;
    gap: 10px;
    text-decoration: none;
  }
  .cta svg { width: 16px; height: 24px; }
  .product {
    position: absolute;
    display: block;
  }
  .product--back { left: 716px; top: 0; width: 350px; height: 294px; }
  .product--front { left: 735px; top: 200px; width: 465px; height: 265px; }
</style>
</head>
<body>
  <section class="banner">
    <h1 class="headline">
      <span class="headline__top">Wireless</span>
      <span class="headline__bottom">Intercoms</span>
    </h1>
    <p class="tagline">Browse Products That Make<br>Wireless Home Communication Easy!</p>
    <a class="cta" href="http://www.brivelloop.example">Shop Now
      <svg viewBox="0 0 16 24" aria-hidden="true"><path d="M3 3 L12 12 L3 21" fill="none" stroke="currentColor" stroke-width="4"/></svg>
    </a>

    <svg class="product product--back" viewBox="0 0 350 294" role="img" aria-label="Photo of a silver and black wireless intercom unit with antenna">
      <defs>
        <linearGradient id="deviceBack" x1="0" y1="0" x2="1" y2="0">
          <stop offset="0" stop-color="#c9c9c9"/>
          <stop offset="0.55" stop-color="#9a9a9a"/>
          <stop offset="0.6" stop-color="#2a2a2a"/>
          <stop offset="1" stop-color="#151515"/>
        </linearGradient>
      </defs>
      <path d="M20 175 Q20 150 60 140 L300 110 Q345 108 348 150 L348 215 Q345 245 300 250 L60 280 Q20 285 20 250 Z" fill="url(#deviceBack)"/>
    </svg>

    <svg class="product product--front" viewBox="0 0 465 265" role="img" aria-label="Photo of a second silver and black wireless intercom unit with antenna">
      <defs>
        <linearGradient id="deviceFront" x1="0" y1="0" x2="1" y2="0">
          <stop offset="0" stop-color="#cdcdcd"/>
          <stop offset="0.58" stop-color="#9d9d9d"/>
          <stop offset="0.63" stop-color="#2a2a2a"/>
          <stop offset="1" stop-color="#141414"/>
        </linearGradient>
      </defs>
      <path d="M0 110 Q0 80 50 70 L420 20 Q465 15 465 60 L465 265 L30 265 Q0 260 0 230 Z" fill="url(#deviceFront)"/>
    </svg>
  </section>
</body>
</html>
```